1923 Basins & Spouts Business Card

I'm wanting to get a business card designed. Our business is 1923 Basins & Spouts
Details for the card:

1923 Basins & Spouts
Name: Gareth Vostle
Email: gareth@1923basinsandspouts.com.au
Website: www.1923basinsandspouts.com.au
Mobile: 0439 602 158
Phone: 02 5550 1843

Font of Basins & Spouts is called Snell Roundhand. Not sue what font logo text is.

I'm thinking two sided but it doesn't have to be.

```html
<!DOCTYPE html>
<html lang="en">
<head>
<meta charset="utf-8">
<title>1923 Basins &amp; Spouts — Business Card</title>
<link rel="stylesheet" href="https://fonts.googleapis.com/css2?family=Mulish:wght@300;400&family=Open+Sans:wght@400&display=swap">
<style>
  :root {
    --backdrop: #c9c9cc;
    --card-front: #ffffff;
    --card-back-top: #3c3c3d;
    --card-back-bottom: #1e1e20;
    --ink: #1c1c1c;
    --ink-soft: #5a5a5a;
    --reverse-ink: #e8e8e8;
    --reverse-ink-soft: #b9b9b9;
  }
  * { margin: 0; padding: 0; box-sizing: border-box; }
  html, body {
    width: 1200px;
    height: 1200px;
    overflow: hidden;
    background: var(--backdrop);
  }
  .sheet {
    position: relative;
    width: 1200px;
    height: 1200px;
    display: flex;
    justify-content: center;
    align-items: center;
    gap: 80px;
  }
  .card {
    position: relative;
    width: 400px;
    height: 654px;
    box-shadow: 0 18px 40px rgba(0, 0, 0, 0.22);
  }
  .card--front {
    background: var(--card-front);
    display: flex;
    flex-direction: column;
    align-items: center;
  }
  .brand-name {
    margin-top: 260px;
    font-family: "Mulish", sans-serif;
    font-weight: 400;
    font-size: 34px;
    line-height: 1.25;
    color: var(--ink);
    text-align: center;
    letter-spacing: 0.5px;
  }
  .tagline {
    margin-top: 34px;
    font-family: "Open Sans", sans-serif;
    font-size: 13.5px;
    color: var(--ink-soft);
    text-align: center;
  }
  .card--back {
    background: linear-gradient(150deg, var(--card-back-top) 0%, var(--card-back-bottom) 70%);
    color: var(--reverse-ink);
    font-family: "Mulish", sans-serif;
    padding: 232px 0 0 74px;
  }
  .person-name {
    font-weight: 400;
    font-size: 30px;
    line-height: 1.1;
  }
  .person-role {
    margin: 4px 0 0 8px;
    font-weight: 300;
    font-size: 14px;
    color: var(--reverse-ink-soft);
  }
  .contact-list {
    list-style: none;
    margin: 26px 0 0 14px;
  }
  .contact-item {
    display: flex;
    align-items: center;
    gap: 14px;
    font-weight: 300;
    font-size: 15.5px;
    height: 30px;
    margin-bottom: 8px;
  }
  .contact-icon {
    width: 16px;
    height: 16px;
    flex: none;
    fill: none;
    stroke: var(--reverse-ink);
    stroke-width: 1.4;
  }
  .contact-icon--solid { fill: var(--reverse-ink); stroke: none; }
</style>
</head>
<body>
<main class="sheet">
  <section class="card card--front" aria-label="Card front">
    <p class="brand-name">1923<br>Basins &amp; Spouts</p>
    <p class="tagline">Combining timeless beauty with perfect practicality</p>
  </section>

  <section class="card card--back" aria-label="Card back">
    <h1 class="person-name">Gareth Vostle</h1>
    <p class="person-role">proprietor</p>
    <ul class="contact-list">
      <li class="contact-item">
        <svg class="contact-icon" viewBox="0 0 16 16" aria-hidden="true"><rect x="1.5" y="3.5" width="13" height="9"/><path d="M1.5 3.5 8 9l6.5-5.5"/></svg>
        gareth@1923basinsandspouts.com.au
      </li>
      <li class="contact-item">
        <svg class="contact-icon" viewBox="0 0 16 16" aria-hidden="true"><circle cx="8" cy="8" r="6.5"/><ellipse cx="8" cy="8" rx="3" ry="6.5"/><path d="M1.5 8h13M2.5 5h11M2.5 11h11"/></svg>
        www.1923basinsandspouts.com.au
      </li>
      <li class="contact-item">
        <svg class="contact-icon contact-icon--solid" viewBox="0 0 16 16" aria-hidden="true"><path d="M1 5c0-2 3-3 7-3s7 1 7 3v1.5h-3.5V5h-7v1.5H1z"/><path d="M4 7h8l2 6H2z"/></svg>
        0439 602 158
      </li>
      <li class="contact-item">
        <svg class="contact-icon" viewBox="0 0 16 16" aria-hidden="true"><rect x="4.5" y="1.5" width="7" height="13" rx="1.2"/><path d="M7 12.5h2"/></svg>
        02 5550 1843
      </li>
    </ul>
  </section>
</main>
</body>
</html>
```